Wordpress Design Project for Employee Communications Site

We need a Wordpress design for a company that strategizes on and produces materials for employee communications. Improving employee communications at all levels of an organization can help improve overall company performance and results. The site needs to look very clean and professional; we're not afraid of white space. We like the functionality that Wordpress provides; however, we only want one "true" blog page; the other pages should give the impression of a more "static" web site - particularly the home page. I have a logo that I can provide.

I have added these comments to the discussion page:
Great question - thank you for asking it. I’ve done more research

I like the very clean and monochromatic looks to many of these. I don’t have to have monochromatic, but I do like minimal colors. Simple, clean, organized. The home page should “fit” almost entirely without scrolling. I do like fat footers that you can scroll down to. I don’t want a colored background, but any that I’ve chosen with colored backgrounds could be switched to a white background.

http://www.moravelkinst.com/
http://pondrix.com/
http://v1.belmarquist.com/
http://howtheotter.com/
http://stayingnimble.com/
http://www.interiors.pelmun.co.uk/
http://brixalumnihub.com/

These last two are more corporate sites. The first one is from a well-respected consultant in my area who does a lot of what I do. And I think Harwick does a nice job with their site. So, I want to marry the look I like with getting the content job done.

http://www.messagefuelworks.com/
http://www.harwick.com/view/en_US/us/index.htm

Target Market(s)

Target market is mid- to large-sized companies. More than 500 employees.

Industry/Entity Type

Communications

Requirements
Must have
• Need an impactful home page. There should be a "blog" page; contact us; services; about. For starters, at least. I want fonts to be very readable - that is, either quite dark gray or black.
Nice to have
• I am loathe to include a picture of myself, but I do want some images that say, "professional" and "expert" in communications.
Should not have
• I don't want a hits counter :) (I know no one would do that!).

```html
<!DOCTYPE html>
<html lang="en">
<head>
<meta charset="utf-8">
<title>Brightwell Workplace Communications</title>
<link rel="stylesheet" href="https://fonts.googleapis.com/css2?family=Source+Sans+3:wght@400;600&family=Yanone+Kaffeesatz:wght@400&display=swap">
<style>
:root{
  --blue:#00adef;
  --blue-dark:#0a8fc9;
  --lime:#c6e21f;
  --lime-dark:#a9c80f;
  --ink:#1f1f1f;
  --muted:#555;
  --line:#bdbdbd;
  --field:#eeeeee;
  --footer:#e0e0e0;
  --white:#ffffff;
}
*{box-sizing:border-box;margin:0;padding:0}
html,body{width:1200px;height:1200px;overflow:hidden;background:var(--white)}
body{position:relative;font-family:"Source Sans 3",Arial,sans-serif;color:var(--ink)}
.band{position:absolute;left:0;width:1200px;background:var(--blue)}
.band-top{top:0;height:14px}
.band-bottom{top:1182px;height:18px}

.brand{position:absolute;left:167px;top:52px;display:flex;align-items:center;gap:12px}
.brand-mark{width:46px;height:46px;border-radius:50%;background:var(--blue)}
.brand-name{font-size:22px;font-weight:400;color:#3b3e8c;line-height:1.05}

.search{position:absolute;left:824px;top:39px;width:201px;height:27px;border:1px solid #ccc;border-radius:14px;
  background:linear-gradient(#fff,#f1f1f1);box-shadow:0 1px 3px rgba(0,0,0,.25);font-size:11px;color:#333;padding:6px 0 0 14px}
.search svg{position:absolute;right:10px;top:6px}

.nav{position:absolute;top:91px;left:576px;display:flex;gap:4px}
.nav a{display:block;width:109px;height:32px;border-radius:6px;background:linear-gradient(var(--lime),var(--lime-dark));
  text-align:center;line-height:32px;font-size:12px;color:#222;text-decoration:none}

.hero{position:absolute;left:170px;top:141px;width:859px;height:381px;border:1px solid var(--blue);
  background:linear-gradient(90deg,#f6f8fa 0%,#eef2f5 35%,#9aa3ab 55%,#4b4f57 75%,#2a2d33 100%)}
.dots{position:absolute;left:566px;top:508px;width:80px;height:15px;background:var(--blue);border-radius:3px 3px 0 0;
  display:flex;justify-content:center;align-items:center;gap:3px}
.dots span{width:9px;height:9px;border-radius:50%;background:#fff}
.dots span.on{background:var(--lime)}

.welcome{position:absolute;left:170px;top:522px;width:858px;height:229px;background:var(--blue)}
.welcome::before{content:"";position:absolute;left:20px;right:20px;top:-14px;height:14px;border-radius:50%;
  box-shadow:0 16px 14px rgba(0,0,0,.45)}
.welcome h2{position:absolute;left:19px;top:30px;font-family:"Yanone Kaffeesatz",sans-serif;font-weight:400;font-size:26px;color:#fff}
.welcome .rule{position:absolute;left:19px;top:62px;width:806px;height:1px;background:rgba(255,255,255,.45)}
.welcome .photo{position:absolute;left:22px;top:83px;width:233px;height:122px;background:linear-gradient(90deg,#f3f3f3,#d7d2cd 50%,#f3f3f3)}
.welcome p{position:absolute;left:275px;top:89px;width:554px;font-size:11.5px;line-height:18.5px;color:#fff;text-align:justify}

.card{position:absolute;top:764px;width:296px;height:177px;border-radius:8px;background:linear-gradient(var(--lime),#b4d414)}
.card::after{content:"";position:absolute;left:25px;right:25px;bottom:-18px;height:16px;border-radius:50%;
  background:radial-gradient(ellipse at center,rgba(0,0,0,.55),rgba(0,0,0,0) 70%)}
.card h3{position:absolute;left:14px;top:10px;font-family:"Yanone Kaffeesatz",sans-serif;font-weight:400;font-size:24px;color:#111}
.card .rule{position:absolute;left:0;right:0;top:42px;height:1px;background:rgba(255,255,255,.5)}
.card-services{left:167px}
.card-blog{left:473px}
.card .thumb{position:absolute;left:14px;top:58px;width:125px;height:95px;border-radius:8px;background:linear-gradient(#e6ddd3,#b99b8a)}
.card .summary{position:absolute;left:157px;top:62px;width:122px;font-size:12px;line-height:16.6px;text-align:justify;color:#111}
.card ul{position:absolute;left:17px;top:56px;width:265px;list-style:none}
.card li{position:relative;padding-left:16px;font-size:11.5px;line-height:16.6px;color:#111;margin-bottom:13px}
.card li::before{content:"";position:absolute;left:2px;top:5px;border-left:4px solid #222;border-top:3px solid transparent;border-bottom:3px solid transparent}
.more{position:absolute;right:15px;top:144px;width:48px;height:21px;border-radius:10px;background:linear-gradient(#20b8f2,var(--blue-dark));
  color:#fff;font-size:11px;text-align:center;line-height:21px}

.newsletter{position:absolute;left:795px;top:764px;width:233px}
.newsletter h3{font-family:"Yanone Kaffeesatz",sans-serif;font-weight:400;font-size:24px;color:#111;margin-top:10px}
.newsletter .rule{position:absolute;left:0;top:42px;width:231px;height:1px;background:var(--line)}
.field{position:absolute;left:1px;width:232px;height:30px;border:1px solid #c9c9c9;background:var(--field);font-size:11.5px;color:#333;padding:7px 10px}
.field-name{top:57px}
.field-mail{top:97px}
.signup{position:absolute;left:152px;top:144px;width:81px;height:27px;background:var(--blue-dark);color:#fff;font-size:16px;text-align:center;line-height:27px}

.footer{position:absolute;left:167px;top:983px;width:864px;height:193px;background:var(--footer)}
.follow{position:absolute;left:340px;top:47px;display:flex;align-items:center;gap:4px;font-size:11.5px}
.follow .label{margin-right:10px}
.social{width:28px;height:28px;border-radius:3px;background:#8a9aa6}
.footer .rule{position:absolute;left:23px;top:100px;width:836px;height:1px;background:#a8a8a8}
.footer-links{position:absolute;left:0;width:100%;top:114px;text-align:center;font-size:11.5px}
.footer-links span{margin:0 7px;color:#333}
.copyright{position:absolute;left:0;width:100%;top:137px;text-align:center;font-size:11.5px}
</style>
</head>
<body>
<div class="band band-top"></div>

<header>
  <div class="brand"><span class="brand-mark"></span><span class="brand-name">Brightwell Workplace<br>Communications</span></div>
  <div class="search">Search
    <svg width="16" height="16" viewBox="0 0 16 16"><circle cx="6" cy="6" r="4.3" fill="none" stroke="#777" stroke-width="1.6"/><path d="M9.2 9.2l5 5" stroke="#777" stroke-width="2.2" stroke-linecap="round"/></svg>
  </div>
  <nav class="nav"><a href="#">About us</a><a href="#">Services</a><a href="#">Blog</a><a href="#">Contact Us</a></nav>
</header>

<div class="hero" role="img" aria-label="Photo of four smiling business colleagues in a bright office"></div>
<div class="dots"><span></span><span class="on"></span><span></span><span></span><span></span></div>

<section class="welcome">
  <h2>Welcome to Our Site</h2>
  <div class="rule"></div>
  <div class="photo" role="img" aria-label="Photo of a team of young professionals"></div>
  <p>Lorem Ipsum is simply dummy text of the printing and typesetting industry. Lorem Ipsum has been the industry's standard dummy text ever since the 1500s, when an unknown printer took a galley of type and scrambled it to make a type specimen book. It has survived not only five centuries, but also the leap into electronic typesetting, remaining essentially unchanged. It was popularised in the 1960s with the release of Lettrafix sheets containing Lorem Ipsum passages, and more recently with desktop publishing software like Quillset Layout including versions of Lorem Ipsum.</p>
</section>

<section class="card card-services">
  <h3>Services</h3>
  <div class="rule"></div>
  <div class="thumb" role="img" aria-label="Photo of a professional woman at her office desk"></div>
  <p class="summary">Lorem Ipsum is simply dummy text of the printing and typesetting industry. Lorem Ipsum has...</p>
  <span class="more">more</span>
</section>

<section class="card card-blog">
  <h3>Our Blog</h3>
  <div class="rule"></div>
  <ul>
    <li>Lorem Ipsum is simply dummy text of the printing and typesetting industry. Lorem Ipsum has...</li>
    <li>Lorem Ipsum is simply dummy text of the printing and typesetting industry. Lorem Ipsum has...</li>
  </ul>
  <span class="more">more</span>
</section>

<section class="newsletter">
  <h3>Sign up Our Newsletter</h3>
  <div class="rule"></div>
  <div class="field field-name">Enter the Name</div>
  <div class="field field-mail">Enter the E mail id</div>
  <span class="signup">Sign Up</span>
</section>

<footer class="footer">
  <div class="follow"><span class="label">Follow Us on</span><span class="social"></span><span class="social"></span><span class="social"></span><span class="social"></span></div>
  <div class="rule"></div>
  <div class="footer-links">About us<span>|</span>Services<span>|</span>Blog<span>|</span>Contact us</div>
  <div class="copyright">Copyrights @ 2012 All Rights Reserved</div>
</footer>

<div class="band band-bottom"></div>
</body>
</html>
```